Dentist Ad for Airline Magazine

A full page print ad for magazine. Details below.

Target Market(s)

Mine workers and rural patients who fly in and out of the main city.

Industry/Entity Type

Airline

Requirements
Must have
• Copywriting as per attachment. Magazine print specifications as per attachment. Inviting colours (blue shades, perhaps some green/yellow). Comforting look and picture. Professional feel. Picture can be of a smiling or sleeping relaxed person (see business websites http://www.calmharbordentalcare.com and http://www.willowbankdentalclinic.com.au) - as we bring patients with complex dental problems or fear of the dentist, back to health whilst they enjoy a relaxing sleep (sedation).
Nice to have
• - stylised image of an aeroplane route across the text or at the footer

```html
<!DOCTYPE html>
<html lang="en">
<head>
<meta charset="utf-8">
<title>Fly-in and Fly-out Dental Transformations – Magazine Ad</title>
<link rel="stylesheet" href="https://fonts.googleapis.com/css2?family=Roboto+Condensed:ital,wght@0,400;0,700;0,800;1,700&display=swap">
<style>
  :root {
    --navy: #1d3b6b;
    --ink: #1f3d72;
    --sky-top: #3f78c4;
    --sky-mid: #7fa8dc;
    --sky-low: #dbe6f2;
    --slate: #6e7f97;
    --yellow-text: #f2e64b;
    --flash: #f6ef1c;
    --white: #ffffff;
    --page: #ffffff;
  }
  * { box-sizing: border-box; margin: 0; padding: 0; }
  html, body { width: 1200px; height: 900px; overflow: hidden; background: var(--page); }
  body { font-family: "Roboto Condensed", "Arial Narrow", sans-serif; position: relative; }

  .ad {
    position: absolute; left: 277px; top: 32px;
    width: 655px; height: 847px;
    background: var(--navy);
    overflow: hidden;
    color: var(--white);
  }

  .hero { position: absolute; left: 0; top: 0; width: 655px; height: 420px; }
  .hero svg { position: absolute; left: 0; top: 0; }
  .hero-headline {
    position: absolute; left: 30px; top: 96px; width: 600px;
    transform: rotate(-3.2deg); transform-origin: left top;
    font-weight: 800; font-size: 26px; line-height: 1.08;
    text-transform: uppercase; letter-spacing: 0.2px;
    text-shadow: 0 1px 2px rgba(0,0,0,.25);
  }

  .questions {
    position: absolute; right: 14px; top: 404px; width: 620px;
    text-align: right; font-weight: 700; font-size: 14.6px; line-height: 18.5px;
  }
  .intro {
    position: absolute; right: 36px; top: 482px; width: 440px;
    text-align: right; color: var(--yellow-text); font-size: 10.6px; line-height: 1.3;
  }

  .why-us { position: absolute; left: 26px; top: 524px; width: 345px; }
  .why-us h2 { font-size: 14.5px; font-weight: 700; margin: 0 0 6px 11px; }
  .why-us ul { list-style: none; font-size: 10.8px; line-height: 12.7px; }
  .why-us li { position: relative; padding-left: 27px; }
  .why-us li::before { content: "•"; position: absolute; left: 12px; top: 0; }

  .promise { position: absolute; left: 413px; top: 566px; width: 200px; }
  .promise h3 { font-size: 14.5px; font-weight: 700; line-height: 1.24; }
  .promise p { margin-top: 14px; width: 190px; font-size: 10.6px; line-height: 1.35; }

  .footer { position: absolute; left: 0; top: 707px; width: 655px; height: 140px; background: var(--white); }
  .call-tab {
    position: absolute; left: 0; top: 0; width: 146px; height: 140px;
    background: var(--slate); border-top-right-radius: 60px;
    padding: 26px 0 0 24px; font-weight: 700; font-size: 15.5px; line-height: 1.05;
  }
  .brand { position: absolute; display: flex; align-items: center; gap: 6px; color: var(--ink); font-size: 15px; font-weight: 400; }
  .brand-dot { width: 16px; height: 16px; border-radius: 50%; background: var(--ink); }
  .brand-clinic { left: 157px; top: 20px; }
  .brand-harbor { left: 348px; top: 20px; }
  .contact { position: absolute; color: var(--ink); font-weight: 700; }
  .contact .main { font-size: 13px; }
  .contact .web { margin-top: 10px; font-size: 10px; line-height: 1.35; }
  .contact-clinic { left: 157px; top: 64px; }
  .contact-harbor { left: 348px; top: 67px; }
  .contact-harbor .main { font-size: 11px; }
  .contact-harbor .web { margin-top: 12px; }

  .flash { position: absolute; left: 0; top: 0; }
  .flash-text {
    position: absolute; left: 527px; top: 771px; width: 150px;
    transform: rotate(-45.5deg); transform-origin: center center;
    color: var(--ink); font-weight: 700; font-style: italic;
    font-size: 12.5px; line-height: 14px; text-align: center; white-space: nowrap;
  }
</style>
</head>
<body>
  <main class="ad">
    <section class="hero">
      <svg width="655" height="420" viewBox="0 0 655 420" role="img" aria-label="Photo: relaxed businessman leaning back in an office chair with his feet on a desk among the clouds, a red phone on the desk and an airliner in the blue sky">
        <defs>
          <linearGradient id="sky" x1="0" y1="0" x2="0" y2="1">
            <stop offset="0" stop-color="var(--sky-top)"/>
            <stop offset="0.55" stop-color="var(--sky-mid)"/>
            <stop offset="1" stop-color="var(--sky-low)"/>
          </linearGradient>
        </defs>
        <polygon points="2,39 627,4 632,346 16,405" fill="url(#sky)" stroke="var(--white)" stroke-width="6" stroke-linejoin="round"/>
      </svg>
      <h1 class="hero-headline">Fly-in and fly-out dental transformations<br>True care, advanced expertise, minimal visits</h1>
    </section>

    <div class="questions">
      Embarassed to Smile? Complex dental problems?<br>
      Do you suffer from fear of the dentist or just can’t find the right one?<br>
      No time for endless appointments?<br>
      Do you wish you could just sleep your way to a healthy and attractive smile?
    </div>
    <p class="intro">If the answer is yes to any of these questions, you are certainly not alone! In our specialized Sleep Dentistry Centre, our renowned team provides gentle, compassionate, advanced and extensive treatments often in the comfort of a relaxing sleep (IV Sedation).</p>

    <section class="why-us">
      <h2>WHY US?</h2>
      <ul>
        <li>We take the time to understand your needs so you can make the best decisions for your health. You are looked after by a friendly, highly qualified expert team in relaxed and comfortable surroundings.</li>
        <li>Our patients often have treatments that would normally take months completed in minimal visits – which is perfect for the Fly-in, Fly-out patient.</li>
        <li>We offer a full range of dental treatments including dental implant surgeries and cosmetic rehabilitations all in-house.</li>
        <li>Our approach with Sleep Dentistry means Pain-Free, anxiety free, memory free procedures. Just excellent results and life changing treatments.</li>
      </ul>
    </section>

    <section class="promise">
      <h3>Sound too good to be true? It’s just what we do for our patients every day</h3>
      <p>Our patients come from all over Western Australia to take advantage of this unique and personalized service. We invite you to let us care for you as well.</p>
    </section>

    <footer class="footer">
      <div class="call-tab">Call our<br>friendly<br>team<br>TODAY</div>
      <div class="brand brand-clinic"><span class="brand-dot"></span><span>Willowbank Dental Clinic</span></div>
      <div class="brand brand-harbor"><span class="brand-dot"></span><span>Calm Harbor Dental Care</span></div>
      <div class="contact contact-clinic">
        <div class="main">T: 9470 5512 / 9470 5513</div>
        <div class="web">www.willowbankdentalclinic.com.au<br>info@willowbankdentalclinic.com.au</div>
      </div>
      <div class="contact contact-harbor">
        <div class="main">42 Harbour Rd Westfield WA 6010</div>
        <div class="web">www.calmharbordentalcare.com<br>info@calmharbordentalcare.com</div>
      </div>
    </footer>

    <svg class="flash" width="655" height="847" viewBox="0 0 655 847" aria-hidden="true">
      <polygon points="482,847 655,847 655,671" fill="var(--flash)"/>
      <line x1="484" y1="845" x2="653" y2="673" stroke="var(--white)" stroke-width="2" stroke-dasharray="2 3"/>
    </svg>
    <div class="flash-text">“Fly-in Fly-out Dental<br>Transformations” (08)<br>T: 9470 5512</div>
  </main>
</body>
</html>
```